Zielgruppe
Beamer Vermietung
Aufgabenstellung
Erstellung 2 professionell aussehender Webseiten.
Projektor-Verleih-Region-Wendlar.de
sowie
Projektor-Verleih-Region-Haselfurtheim.de
Die Seiten sind aktuell im Betrieb, aber haben ein sehr veraltetes Design.
Die Seiten können ähnlich aussehen, sollten aber etwas unterschiedlich sein, damit sie für den Kunden leicht anders aussehen.
Wichtig ist, dass alle Seiten, inklusive Startseite, Unterseiten und Links designed werden und das dieses Design in die bestehende Wordpress Installation eingepflegt wird.
Es ist also notwendig, gute Wordpress Kenntnisse zu haben um dann auch zwei fertige Wordpress Seiten liefern zu können.

```html
<!DOCTYPE html>
<html lang="de">
<head>
<meta charset="utf-8">
<title>Projektor-Verleih Region Wendlar</title>
<link href="https://fonts.googleapis.com/css2?family=Roboto:wght@300;400;500;700;900&family=Roboto+Condensed:wght@400;700&display=swap" rel="stylesheet">
<style>
:root{
  --navy:#2c3e5c;
  --navy-dark:#2e4462;
  --green:#8dc04a;
  --grey-bar:#ececec;
  --grey-strip:#efefef;
  --text-light:#6a6a6a;
  --white:#ffffff;
}
*{margin:0;padding:0;box-sizing:border-box}
html,body{width:763px;height:1200px;overflow:hidden;background:var(--white)}
body{position:relative;font-family:"Roboto",Arial,sans-serif;color:var(--navy)}
.abs{position:absolute}
.topbar{left:0;top:0;width:763px;height:19px;background:var(--grey-bar);border-bottom:1px solid #dcdcdc}
.topbar__url{left:104px;top:5px;font-size:7px;color:#555}
.social{top:5px;width:10px;height:10px;border-radius:50%;background:var(--navy)}
.social--active{background:var(--green)}
.site-title{left:102px;top:30px;font-family:"Roboto Condensed",Arial,sans-serif;font-size:18px;color:var(--green)}
.header-link{top:36px;font-size:8.5px;font-weight:500;color:var(--navy)}
.nav{left:0;top:64px;width:763px;height:31px;background:var(--navy-dark)}
.nav__item{top:0;height:31px;line-height:31px;font-size:9px;font-weight:500;color:var(--white)}
.nav__item--active{background:var(--green);color:var(--navy);padding:0 6px 0 8px}
.hero{left:0;top:95px;width:763px;height:293px;background:linear-gradient(100deg,#5a5048 0%,#8a7460 40%,#6c6660 70%,#9aa7ae 100%)}
.hero__rule{left:102px;top:163px;width:18px;height:1.5px;background:var(--white)}
.hero__title{left:102px;top:167px;font-size:31px;font-weight:700;line-height:35px;color:var(--white)}
.hero__sub{left:102px;top:237px;font-size:16.5px;font-weight:500;color:var(--white)}
.btn{background:var(--green);border-radius:12px;text-align:center;font-weight:500;color:var(--white)}
.hero__btn{left:103px;top:296px;width:90px;height:23px;line-height:23px;font-size:9px;color:var(--navy);letter-spacing:.3px}
.strip{left:0;top:388px;width:763px;height:53px;background:var(--grey-strip)}
.strip__text{left:114px;top:404px;font-size:18px;font-weight:900;color:var(--navy);white-space:nowrap}
.price{display:inline-block;width:38px;height:38px;line-height:38px;border-radius:50%;background:var(--green);text-align:center;margin:-10px 1px}
.intro{left:0;top:460px;width:763px;text-align:center;font-size:18px;font-weight:300;line-height:24px;color:var(--navy)}
.product__title{font-size:22px;font-weight:700;color:var(--navy);line-height:27px}
.product__line{font-size:22px;font-weight:300;color:var(--text-light);line-height:27px}
.product__line--small{font-size:18px}
.product__btn{width:71px;height:24px;line-height:24px;font-size:9px}
.product__image{background:radial-gradient(ellipse at center,#b7b9bd 0%,#d9dadc 45%,#ffffff 75%)}
.footer{left:0;top:1063px;width:763px;height:108px;background:linear-gradient(115deg,#2b3e5c 0%,#354b6b 55%,#2d415f 100%)}
.footer__cta{left:101px;top:1101px;font-size:26px;font-weight:500;color:var(--green)}
.footer__tel{left:487px;top:1106px;font-size:21px;font-weight:300;color:var(--white)}
.copyright{left:0;top:1171px;width:763px;height:29px;background:var(--green);text-align:center;line-height:29px;font-size:7px;color:var(--navy)}
</style>
</head>
<body>

<div class="abs topbar"></div>
<div class="abs topbar__url">www.projektor-verleih-region-wendlar.de</div>
<div class="abs social social--active" style="left:589px"></div>
<div class="abs social" style="left:608px"></div>
<div class="abs social" style="left:627px"></div>
<div class="abs social" style="left:646px"></div>

<div class="abs site-title">Beamer Vermietung zu Günstigen Konditionen</div>
<svg class="abs" style="left:516px;top:37px" width="13" height="9" viewBox="0 0 13 9"><rect x=".5" y=".5" width="12" height="8" fill="none" stroke="#2c3e5c"/><path d="M.5 .5 6.5 5 12.5 .5" fill="none" stroke="#2c3e5c"/></svg>
<div class="abs header-link" style="left:535px">Kontakt / Anreise</div>
<div class="abs header-link" style="left:616px">Impressum</div>

<nav class="abs nav">
  <div class="abs nav__item nav__item--active" style="left:103px">Startseite</div>
  <div class="abs nav__item" style="left:162px">Beamer mieten</div>
  <div class="abs nav__item" style="left:237px">HD-Beamer mieten</div>
  <div class="abs nav__item" style="left:329px">Full HD-Beamer</div>
  <div class="abs nav__item" style="left:406px">Leinwand mieten</div>
  <div class="abs nav__item" style="left:489px">Reservierung</div>
  <div class="abs nav__item" style="left:556px">Preisliste</div>
  <div class="abs nav__item" style="left:606px">Datenschutz</div>
</nav>

<div class="abs hero" role="img" aria-label="Foto: Beamer auf einem Besprechungstisch, unscharfer Seminarraum im Hintergrund"></div>
<div class="abs hero__rule"></div>
<h1 class="abs hero__title">&nbsp;! Beamer mieten zu<br>TOP-Konditionen !</h1>
<div class="abs hero__sub">NEU: Jetzt auch HD-Beamer!</div>
<div class="abs btn hero__btn">KONTAKT</div>

<div class="abs strip"></div>
<svg class="abs" style="left:70px;top:400px" width="40" height="30"><circle cx="11" cy="20" r="8" fill="#8dc04a"/><circle cx="28" cy="8" r="3.5" fill="#2c3e5c"/></svg>
<div class="abs strip__text">Beamer-Vermietung im Raum Wendlar / Kobental&nbsp; für nur<span class="price">€30</span>/ Tag</div>

<p class="abs intro">Jetzt neu: HD-Beamer für das<br>perfekte Bilderlebnis zu günstigen Konditionen!</p>

<div class="abs" style="left:104px;top:553px">
  <h2 class="product__title">Beamer mieten</h2>
  <p class="product__line">Informationen zum Modell:</p>
  <p class="product__line">Beamer Modell Lumaro LX520</p>
</div>
<div class="abs btn product__btn" style="left:103px;top:649px">Weiterlesen</div>
<div class="abs product__image" style="left:448px;top:540px;width:214px;height:145px" role="img" aria-label="Produktfoto: dunkelgrauer Beamer"></div>

<div class="abs product__image" style="left:103px;top:712px;width:207px;height:98px" role="img" aria-label="Produktfoto: weißer HD-Beamer"></div>
<div class="abs" style="left:338px;top:714px">
  <h2 class="product__title">HD Beamer mieten</h2>
  <p class="product__line">Informationen zum Modell:</p>
  <p class="product__line" style="font-size:21px">HD-Beamer Modell Vistrel V70</p>
</div>
<div class="abs btn product__btn" style="left:339px;top:803px">Weiterlesen</div>

<div class="abs" style="left:104px;top:871px">
  <h2 class="product__title">Full-HD Beamer mieten</h2>
  <p class="product__line">Informationen zum Modell:</p>
  <p class="product__line product__line--small">Full-HD-Beamer Modell Kestrava FX9</p>
</div>
<div class="abs btn product__btn" style="left:103px;top:966px">Weiterlesen</div>
<div class="abs product__image" style="left:443px;top:868px;width:219px;height:122px" role="img" aria-label="Produktfoto: weißer Full-HD-Beamer"></div>

<footer class="abs footer"></footer>
<div class="abs footer__cta">Reservieren oder Buchen</div>
<svg class="abs" style="left:454px;top:1111px" width="22" height="16" viewBox="0 0 22 16"><path d="M1 6C1 1 21 1 21 6v2h-5V5H6v3H1z" fill="#8dc04a"/><path d="M5 8h12l3 7H2z" fill="#8dc04a"/><circle cx="11" cy="11" r="2.4" fill="#2e4462"/></svg>
<div class="abs footer__tel">Tel: 0160 / 5550123</div>
<div class="abs copyright">Copyright © 2020.&nbsp; Projektor-verleih-region-wendlar.de</div>

</body>
</html>
```